Login screen design for grocery app

Hi,

We are working on a grocery delivery app and need a design for its launch screen. This is the screen where the user clicks on either Login or Register. You can see our current login screen (and app name) in the attached image. You should use the same background color.

We are looking for designs that have to do with groceries (fruits/vegetables/diary products/chocolate etc).

Note: We do not want a login form on the launch screen, only a Login and Register button.

Let me know if you have any questions.

Regards.

Industry/Entity Type

Grocery Store

Colors
886aae
6b449b
e34298
ffffff
9bcb3c
f78f20
f04a50
33b8a4
34a6d7

Requirements
Must have
• The design must have to do with groceries.

```html
<!DOCTYPE html>
<html lang="en">
<head>
<meta charset="utf-8">
<title>Cartly – Launch Screen</title>
<link href="https://fonts.googleapis.com/css2?family=Open+Sans:wght@300;400;600;700&display=swap" rel="stylesheet">
<style>
  :root {
    --stage: #27282a;
    --brand-purple: #693cb7;
    --white: #ffffff;
    --cart-green: #33b8a4;
    --cart-orange: #f78f20;
    --cart-yellow: #f6d21c;
    --cart-red: #f04a50;
    --cart-grey: #e6e6e6;
  }
  * { box-sizing: border-box; margin: 0; padding: 0; }
  html, body {
    width: 1200px;
    height: 998px;
    overflow: hidden;
    background: var(--stage);
    font-family: "Open Sans", Arial, sans-serif;
  }
  .launch-screen {
    position: absolute;
    left: 330px;
    top: 19px;
    width: 541px;
    height: 960px;
    background: var(--brand-purple);
    color: var(--white);
    box-shadow: 0 8px 30px rgba(0,0,0,0.35);
  }
  .status-bar {
    position: absolute;
    top: 6px;
    left: 10px;
    right: 10px;
    height: 26px;
    display: flex;
    align-items: center;
    justify-content: space-between;
    font-size: 19px;
  }
  .status-bar .signal { display: flex; gap: 3px; }
  .status-bar .signal span {
    width: 9px; height: 9px; border-radius: 50%; background: var(--white);
  }
  .status-bar .clock { font-weight: 700; position: absolute; left: 50%; transform: translateX(-50%); }
  .status-bar .battery-group { display: flex; align-items: center; gap: 6px; }
  .status-bar .battery {
    width: 38px; height: 16px; border: 2px solid var(--white); border-radius: 3px; padding: 1px; position: relative;
  }
  .status-bar .battery::before { content: ""; display: block; width: 100%; height: 100%; background: var(--white); }
  .status-bar .battery::after {
    content: ""; position: absolute; right: -5px; top: 4px; width: 3px; height: 5px; background: var(--white);
  }
  .app-name {
    position: absolute;
    top: 160px;
    left: 0;
    width: 100%;
    text-align: center;
    font-weight: 300;
    font-size: 92px;
    letter-spacing: 2px;
    line-height: 1;
  }
  .cart-illustration {
    position: absolute;
    left: 105px;
    top: 317px;
    width: 310px;
    height: 279px;
    border-radius: 18px;
    background: linear-gradient(160deg, var(--cart-orange) 0%, var(--cart-yellow) 30%, var(--cart-green) 55%, var(--cart-red) 75%, var(--cart-grey) 100%);
    opacity: 0.9;
  }
  .auth-button {
    position: absolute;
    left: 139px;
    width: 262px;
    height: 67px;
    border-radius: 34px;
    display: flex;
    align-items: center;
    justify-content: center;
    font-size: 20px;
    font-weight: 700;
    letter-spacing: 2px;
    box-shadow: 0 4px 10px rgba(0,0,0,0.18);
  }
  .auth-button--login { top: 651px; background: var(--white); color: var(--brand-purple); }
  .auth-button--register { top: 762px; border: 3px solid var(--white); color: var(--white); background: transparent; }
</style>
</head>
<body>
  <main class="launch-screen">
    <div class="status-bar">
      <div class="signal"><span></span><span></span><span></span><span></span><span></span></div>
      <div class="clock">10:30 PM</div>
      <div class="battery-group"><span>100%</span><div class="battery"></div></div>
    </div>
    <h1 class="app-name">Cartly</h1>
    <div class="cart-illustration" role="img" aria-label="Illustration of a speeding shopping cart filled with groceries: bottle, bread, bananas, watermelon and vegetables"></div>
    <div class="auth-button auth-button--login">LOGIN</div>
    <div class="auth-button auth-button--register">REGISTER</div>
  </main>
</body>
</html>
```